Ecommerce brand for entrepreneurs needs help with branding products

I am looking for help to design a small supplement pouch. Including colours, layout and design.

The business:
The business is called 'Keel Orbit' and our goal is to help entrepreneurs continue to change the world in spite of how difficult it is.

At Keel Orbit, we understand being an entrepreneur is one of the hardest jobs there is. We believe there is a better way. A way in which you don’t have to choose between success in your business and the rest of your life. Our aim is to solve these challenges, so you can stay in the fight a little longer. If we can do this, we can ultimately change the world into a better place.

We will do this through a range of supplements, community, information and physical products to help you optimise their lives.

The product:
The product I am looking to create is for a natural nootropic called

‘The Velvet Compass’

The product will address the challenges with focus and lower attention spans.

So Entrepreneurs can Solve more problems, Help more people and make more money.

Do more in four hours than a whole day. Have Zen like calm. With Zero Jitters & Zero Crashes. Do what others can’t

The design:
I want this to be a small pouch. The final design should be elegant, and minimalist and have an edge that is different.

I have added examples of products that I like below.

I am open to most colour combinations but silver, navy, black, orange, white and translucent are what is taking my fancy right now.

I like the idea of having a translucent package or part of the package like some of the designs below. I also like the matt finish of some of the designs along with the flashes of shininess from silver for contrast. or even using embossing within the packaging.

I have a logo that I have made but I am open to changes on that as well if you see fit. if you do want to do this, I would love to see an emblem next to the words Keel Orbit that encapsulates the brand.

I have done some really really rough mockups myself but would like to see what you have to offer rather than what I have done

The purpose of this image:
I need a 3D mockup of this supplement to be on my landing page to start to take pre-orders.

I am ideally looking for 2 images

1) Supplement packaging on its own
2) Supplement packaging with background coloured lighting, with powder on the ground etc

Need extra days to review

Target Market(s)

The logo: Please also redesign my logo - I would love to see an emblem next to the words Keel Orbit that encapsulates the brand.The business is called 'Keel Orbit' and our goal is to help entrepreneurs continue to change the world in spite of how difficult it is. At Keel Orbit, we understand being an entrepreneur is one of the hardest jobs there is. We believe there is a better way. A way in which you don’t have to choose between success in your business and the rest of your life. Our aim is to solve these challenges, so you can stay in the fight a little longer. If we can do this, we can ultimately change the world into a better place. We will do this through a range of supplements, community, information and physical products to help you optimise their lives.

Industry/Entity Type

Supplements for entrepreneurs

Colors

Requirements
Must have
• The design: I want this to be a small pouch. The final design should be elegant, and minimalist and have an edge that is different. I have added examples of products that I like below. I am open to most colour combinations but silver, navy, black, orange, white and translucent are what is taking my fancy right now. I like the idea of having a translucent package or part of the package like some of the designs below. I also like the matt finish of some of the designs along with the flashes of shininess from silver for contrast. or even using embossing within the packaging.

```html
<!DOCTYPE html>
<html lang="en">
<head>
<meta charset="utf-8">
<title>Keel Orbit — The Velvet Compass Pouch</title>
<link href="https://fonts.googleapis.com/css2?family=Montserrat:wght@300;600;700&family=Playfair+Display:wght@400&family=Oswald:wght@400;500&display=swap" rel="stylesheet">
<style>
  :root {
    --backdrop: #05051a;
    --navy: #1d2a4e;
    --navy-deep: #1a2647;
    --slate: #3d5f72;
    --teal: #6db4a9;
    --white: #f4f6f6;
    --soft: #c9d2dc;
    --orange: #e5801f;
  }
  * { margin: 0; padding: 0; box-sizing: border-box; }
  html, body {
    width: 1200px; height: 2272px; overflow: hidden;
    background: var(--backdrop);
  }
  .canvas { position: relative; width: 1200px; height: 2272px; }
  .pouch {
    position: absolute; left: 200px; top: 575px;
    width: 800px; height: 1122px;
    background: var(--navy);
    overflow: hidden;
  }
  .pouch-top {
    position: absolute; left: 0; top: 0; width: 100%; height: 139px;
    background: var(--navy);
  }
  .slogan {
    position: absolute; top: 28px; width: 100%; text-align: center;
    font-family: 'Montserrat', sans-serif; font-weight: 300;
    font-size: 20px; letter-spacing: 14px; color: var(--soft);
  }
  .zipper {
    position: absolute; left: 0; top: 133px; width: 100%; height: 6px;
    background: #2c3b60; border-top: 1px solid #3a4a70;
  }
  .pouch-body {
    position: absolute; left: 0; top: 139px; width: 100%; height: 586px;
    background: linear-gradient(to bottom, #253559 0%, var(--slate) 35%, #5a9a98 70%, var(--teal) 88%, var(--teal) 100%);
  }
  .pouch-base {
    position: absolute; left: 0; top: 725px; width: 100%; height: 397px;
    background: var(--navy-deep);
  }
  .brand {
    position: absolute; left: 134px; top: 250px;
    display: flex; align-items: center; gap: 10px;
    font-family: 'Montserrat', sans-serif; font-weight: 600;
    font-size: 30px; color: var(--white);
  }
  .brand-mark { width: 26px; height: 26px; border: 4px solid var(--white); }
  .product-title {
    position: absolute; left: 0; top: 360px; width: 100%;
    text-align: center; color: var(--white);
    font-family: 'Montserrat', sans-serif; font-weight: 700;
  }
  .product-title .title-line { font-size: 78px; line-height: 1.12; }
  .product-title .title-rule {
    width: 120px; height: 3px; background: var(--white);
    margin: 22px auto 0;
  }
  .benefits {
    position: absolute; top: 770px; width: 100%; text-align: center;
    font-family: 'Playfair Display', serif; color: var(--white);
  }
  .benefits .pillars { font-size: 54px; line-height: 1.1; }
  .benefits .audience { font-size: 33px; margin-top: 4px; }
  .product-facts {
    position: absolute; left: 142px; top: 945px;
    font-family: 'Oswald', sans-serif; font-weight: 500;
    font-size: 24px; line-height: 34px; color: var(--white);
  }
  .product-facts .flavour-name { color: var(--orange); }
  .product-facts .servings { font-weight: 400; }
</style>
</head>
<body>
<div class="canvas">
  <div class="pouch">
    <div class="pouch-top">
      <p class="slogan">DO WHAT OTHERS CAN'T</p>
    </div>
    <div class="zipper"></div>
    <div class="pouch-body"></div>
    <div class="pouch-base"></div>

    <div class="brand"><span class="brand-mark"></span>Keel Orbit</div>

    <div class="product-title">
      <p class="title-line">The Velvet</p>
      <p class="title-line">Compass</p>
      <div class="title-rule"></div>
    </div>

    <div class="benefits">
      <p class="pillars">Flow - Clarity - Drive</p>
      <p class="audience">For Founders &amp; Entrepreneurs</p>
    </div>

    <div class="product-facts">
      <p>A NATURAL NOOTROPIC</p>
      <p><span class="flavour-name">ORANGE &amp; MANGO</span> FLAVOUR</p>
      <p><span>240g</span> <span class="servings">(30 Servings)</span></p>
    </div>
  </div>
</div>
</body>
</html>
```